Design Harvest Depot a new Menu

I am seeking a designer to provide our company a fresh new menu look

I have attached our current menu, along with our style guide and logos.

I wouldn't mind seeing some fresh fruit and or stock image options

The menu will be used on a back lit menu board and on flyers etc

our competitiors http://www.lemvaro.com.au/ and quillpress.com.au

Our corporate font is bariol

our website

www.harvestdepot.com

I would like the following to be changed

Please use the ingredients for each super smoothie and protein shake instead of the cartoon logo 

images for the protein shakes please use different colour protein powders to add colour to the mix 

for example make a collage/combine the following images for the amber crunch 

http://www.pictoravel.com/pic-482917365/stock-photo-cocoa-nibs-isolated-on-white.html?src=QwPn4L7R_zkTT21ByHHmVc-1-3

http://www.pictoravel.com/pic-57190428/stock-photo-honeycomb-close-up-on-the-white.html?src=HLm4qZTb8KfoW3cVe61rrA-1-4

http://www.pictoravel.com/pic-264810573/stock-photo-chia-seed-over-white.html?src=gtBvKcRmYaPqW8sFnTjHdk-1-32

http://www.pictoravel.com/pic-31649082/stock-photo-peanut-butter-isolated-on-white.html?src=p-270615394-7

http://www.pictoravel.com/pic-48027613/stock-photo-a-scoop-of-chocolate-whey-isolate-protein-isolated-on-white-background.html?src=p-61947205-3

Please use these images as a guide and make them look like they are all together 

Please also remove the Blend on demand menu 

And replace it with KO Dishes 

Acai Bowl 

Acai with guarna, coconut water, banana, toasted muesli, blueberries, shredded coconut, honey 

Regular $10 *add extra, banana, strawberries or blueberries only $1 each 

Pink Pitaya Bowl 

Pink Pitaya, almond milk, banana, toasted muesli, strawberries, shredded coconut, honey 

I would also like to add another protein super smoothie 

Plant Parade 

Coconut Water, Vermela Vegetable Protein Powder, Blueberries, Banana, Cinnamon, Walnuts, Chia Seeds, Antioxidant Mix (contains pomegranate, maqui, acai, blueberry, elderflower and green tea powder)

R $9.95 L$10.95

```html
<!DOCTYPE html>
<html lang="en">
<head>
<meta charset="utf-8">
<title>Harvest Depot Menu</title>
<link href="https://fonts.googleapis.com/css2?family=Nunito:wght@700;800&family=Source+Sans+3:wght@400;600&display=swap" rel="stylesheet">
<style>
:root{
  --ink:#2b3a4a; --text:#222; --teal:#4dbfb0; --rule:#c9ccd1; --footer:#2e3a46;
  --red:#d7262e; --orange:#f07c1a; --yellow:#e8b21c; --green:#7bb83a; --plum:#4a2a3a;
  --kick:#6b3fa0; --recovery:#f08a1c; --shredder:#2d5fa8; --muscle:#d81b60; --lunch:#6cc04a; --energizer:#5b2a1f;
  --berry:#8a8f99; --amber:#7fb5e0; --banana:#7a3b8f; --mango:#f3a640; --forever:#e55a2b; --plant:#3f9a5a;
  --acai:#5e2a6e; --pitaya:#e0245e; --grey:#8a8a8a;
}
*{margin:0;padding:0;box-sizing:border-box}
html,body{width:800px;height:1200px;overflow:hidden;background:#fff}
body{position:relative;font-family:"Source Sans 3",Arial,sans-serif;color:var(--text)}
.abs{position:absolute;line-height:1.15}
.brand{left:0;width:800px;top:14px;text-align:center;font-family:"Nunito",Arial,sans-serif;font-weight:800;font-size:44px;color:var(--ink);letter-spacing:-1px}
.tagline{left:0;width:800px;top:61px;text-align:center;font-size:15px;color:#444}
.fruit-strip{left:0;top:90px;width:800px;height:210px;display:flex}
.fruit-strip div{flex:1;border-top:6px solid}
.note{left:45px;top:321px;font-size:11px}
.section{font-family:"Nunito",Arial,sans-serif;font-weight:700;font-size:18px;color:var(--teal)}
.item{left:46px;width:400px}
.item .icon{position:absolute;left:0;top:4px;width:26px;height:26px;border-radius:50%}
.item .name{position:absolute;left:37px;top:0;font-weight:600;font-size:13px;padding-right:30px;border-bottom:1px solid var(--rule);min-width:108px;padding-bottom:1px;white-space:nowrap}
.item .price{position:absolute;left:304px;top:0;font-size:13px;font-weight:600;white-space:nowrap}
.item .desc{position:absolute;left:37px;top:20px;width:370px;font-size:12px;line-height:1.4;color:var(--text)}
.divider{left:469px;top:348px;width:1px;height:800px;background:#bfe3de}
.right{left:497px;width:290px}
.right h3{font-family:"Nunito",Arial,sans-serif;font-weight:700;font-size:17px}
.right .section{font-size:18px}
.right .desc{font-size:12px;line-height:17.5px;margin-top:4px}
.right .price{font-size:13px;font-weight:600;margin-top:4px}
.right .extra{font-size:12px;line-height:17px;margin-top:14px;color:#555}
.right .sizes{font-size:13px;margin-top:6px}
.photo-frame{left:548px;top:900px;width:170px;height:138px;border:5px solid #1f2b3a;transform:rotate(-2deg);box-shadow:2px 3px 6px rgba(0,0,0,.35)}
.photo-frame svg{display:block}
.credit{left:497px;top:1056px;font-size:11px}
.sign{left:625px;top:1082px;width:145px;height:80px}
.sign .surname{position:absolute;left:35px;top:36px;color:var(--red);font-size:11px;letter-spacing:2px}
.footer{left:0;top:1172px;width:800px;height:28px;background:var(--footer)}
</style>
</head>
<body>
<div class="abs brand">Harvest Depot</div>
<div class="abs tagline">supporting healthy lifestyles</div>

<div class="abs fruit-strip">
  <div role="img" aria-label="Close-up photo of fresh strawberries" style="border-color:var(--red);background:linear-gradient(135deg,#e0323b,#a8141c)"></div>
  <div role="img" aria-label="Close-up photo of oranges" style="border-color:var(--orange);background:linear-gradient(135deg,#f7a03a,#e06a12)"></div>
  <div role="img" aria-label="Close-up photo of lemons" style="border-color:var(--yellow);background:linear-gradient(135deg,#f6d25a,#d99c1a)"></div>
  <div role="img" aria-label="Close-up photo of sliced kiwi fruit" style="border-color:var(--green);background:linear-gradient(135deg,#a6d24a,#5f8f22)"></div>
  <div role="img" aria-label="Close-up photo of blackberries" style="border-color:var(--plum);background:linear-gradient(135deg,#6b4a5a,#2e1c26)"></div>
</div>

<div class="abs note">* All Protein “Shakes” available in Chocolate, Strawberry, Banana &amp; Vanilla</div>

<div class="abs section" style="left:80px;top:346px">Protein “Shakes”</div>

<div class="abs item" style="top:372px;color:var(--kick)"><span class="icon" style="background:var(--kick)"></span><span class="name">Kick Start</span><span class="price">R $5.95 &nbsp;L $6.95</span><span class="desc">Protein, Protein Frozen Yoghurt, Water, Caffeine</span></div>
<div class="abs item" style="top:424px;color:var(--recovery)"><span class="icon" style="background:var(--recovery)"></span><span class="name">Recovery</span><span class="price">R $6.95 &nbsp;L $7.95</span><span class="desc">Protein, Protein Frozen Yoghurt, Water, L- Glutamine, Vitamin C Powder</span></div>
<div class="abs item" style="top:476px;color:var(--shredder)"><span class="icon" style="background:var(--shredder)"></span><span class="name">Shredder</span><span class="price">R $7.95 &nbsp;L $8.95</span><span class="desc">Protein, Protein Frozen Yoghurt, Water, Thermogenic tablet, L-Carnatine, Vitamin C Powder, Chia Seeds</span></div>
<div class="abs item" style="top:543px;color:var(--muscle)"><span class="icon" style="background:var(--muscle)"></span><span class="name">Muscle Maker</span><span class="price">R $8.95 &nbsp;L $9.95</span><span class="desc">Protein, Protein Frozen Yoghurt, Full Cream Milk, Dextrose, Flaxseed Oil, Creatine Monohydrate</span></div>
<div class="abs item" style="top:611px;color:var(--lunch)"><span class="icon" style="background:var(--lunch)"></span><span class="name">Liquid Lunch</span><span class="price">R $7.95 &nbsp;L $8.95</span><span class="desc">Protein, Protein Frozen Yoghurt, Water, LSA Mix, Superfine Oats</span></div>
<div class="abs item" style="top:663px;color:var(--energizer)"><span class="icon" style="background:var(--energizer)"></span><span class="name">Energizer</span><span class="price">R $5.95 &nbsp;L $6.95</span><span class="desc">Protein frozen yoghurt, water and a shot of coffee available in either mocha or latte</span></div>

<div class="abs section" style="left:84px;top:732px">Protein Super Smoothies</div>

<div class="abs item" style="top:756px;color:var(--berry)"><span class="icon" style="background:var(--berry)"></span><span class="name">Berry Sweet</span><span class="price" style="color:var(--text)">R $9.95 &nbsp;L $10.95</span><span class="desc">Strawberries and Cream Protein Powder, Mixed Berries, Acai Powder, Organic Coconut, Ice, Goji Berries, Cranberries, Shredded Coconut</span></div>
<div class="abs item" style="top:818px;color:var(--amber)"><span class="icon" style="background:var(--amber)"></span><span class="name">Amber Crunch</span><span class="price">R $9.95 &nbsp;L $10.95</span><span class="desc">Chocolate Protein Powder, Natural Peanut Butter, Chia Seeds, Manuka Honey, Ice, Cocoa Nibs</span></div>
<div class="abs item" style="top:880px;color:var(--banana)"><span class="icon" style="background:var(--banana)"></span><span class="name">Banana Bliss</span><span class="price">R $9.95 &nbsp;L $10.95</span><span class="desc">Banana Protein Powder, Fresh Banana, Cacoa Nibs, Manuka Honey, Ice, Chia Seeds, Walnuts, Cinnamon</span></div>
<div class="abs item" style="top:942px;color:var(--mango)"><span class="icon" style="background:var(--mango)"></span><span class="name">Mango Oxidant</span><span class="price">R $9.95 &nbsp;L $10.95</span><span class="desc">Vanilla Protein Powder, Mango, Almond Flakes, Organic Honey, Ice, Chia Seeds</span></div>
<div class="abs item" style="top:1004px;color:var(--forever)"><span class="icon" style="background:var(--forever)"></span><span class="name">Forever Energy</span><span class="price">R $9.95 &nbsp;L $10.95</span><span class="desc">Vanilla Protein Powder, Coconut Water, Almond Flakes, Avocado, Chia Seeds, Banana, &nbsp;Dates, Ice, Cacoa Nibs, Acai Berry Powder</span></div>
<div class="abs item" style="top:1066px;color:var(--plant)"><span class="icon" style="background:var(--plant)"></span><span class="name">Plant Parade</span><span class="price">R $9.95 &nbsp;L $10.95</span><span class="desc">Coconut Water, Vermela Vegetable Protein Powder, Blueberries, Banana, Cinnamon, Walnuts, Chia Seeds, Antioxidant Mix (contains pomegranate, maqui, acai, blueberry, elderflower and green tea powder)</span></div>

<div class="abs divider"></div>

<div class="abs right" style="top:346px">
  <h3 class="section">KO Dishes</h3>
  <h3 style="color:var(--acai);margin-top:12px">Acai Bowl</h3>
  <div class="desc">Acai with guarna, coconut water, banana, toasted muesli, blueberries, shredded coconut, honey</div>
  <div class="price">Regular $10</div>
  <h3 style="color:var(--pitaya);margin-top:16px">Pink Pitaya Bowl</h3>
  <div class="desc">Pink Pitaya, almond milk, banana, toasted muesli, strawberries, shredded coconut, honey</div>
  <div class="price">Regular $10</div>
  <div class="extra">*add extra, banana, strawberries or blueberries only $1 each</div>

  <h3 class="section" style="margin-top:30px">Protein Frozen Yoghurt</h3>
  <div class="desc">Our unique Protein Frozen Yoghurt is a Delicious Low Calorie Snack, with over 10 grams of protein per 100 gram serving.</div>
  <div class="sizes"><b>S</b> $4.50 &nbsp;&nbsp;&nbsp;<b>M</b> $6.00 &nbsp;&nbsp;&nbsp;<b>L</b> $7.50</div>
</div>

<div class="abs photo-frame">
  <svg width="160" height="128" role="img" aria-label="Photo of a nutritionist in a white coat holding a green apple">
    <rect width="160" height="128" fill="#eef1f3"/>
    <rect x="50" y="0" width="70" height="128" fill="#dfe4e8"/>
  </svg>
</div>

<div class="abs credit">Our Menu is proudly developed by leading Nutritionist</div>
<div class="abs sign">
  <svg width="145" height="80" role="img" aria-label="Handwritten signature of Corin Valdane">
    <rect x="0" y="0" width="145" height="34" rx="4" fill="#f1f1f1"/>
  </svg>
  <span class="surname">VALDANE</span>
</div>

<div class="abs footer"></div>
</body>
</html>
```